Web Design for High End Baby Products Gear

We have some work from a designer that just didn't meet standards despite weeks of back and forth. We need someone who can come up with creative colors/fonts/etc. to make the site "pop" and give a clean, inviting feel.

We need three pages designed:

1. Home
2. Category Landing Page
3. Product Detail Page

The current site is www.HappyWheelWalks.com

Please DO NOT use current site for inspiration.

The layout should follow pretty close to what we have attached.

We were not even pleased with the logo so for now we are just concentrating on the colors and aesthetic feel of the site. You can use a nice typography type logo. We will probably have the logo done at a later time. Or if you have any ideas please feel free to submit as it may increase chances of winning design. The layout is pretty much done with the product page layout approved by our paid search people.

This is isn't where you need to spend a lot of time with general layout as it is already pretty much complete but you are free to deviate or make suggestions if you think it will help.

Reason: I haven't been able to provide adequate feedback and want to spend appropriate amount of time doing so.

I posted the set of PSD files that the previous designer completed.  We were not happy with the outcome of this.

I said in my brief "Here are a few like companies:

www.pramvault.com
www.buggynest.com
www.tiddlytopkids.com
www.kplums.com
www.wrenandtilly.com
www.doravimo.com"

What I meant was that these were similar companies to our company with respect to product/customer demographic/etc.

Reason: We have found a few that we really like and are working to determine which designs to continue with.

Thank you for your patience.

Reason: Waiting on feedback from a couple of designers so extending deadline

Thank you all.  We received several designs we really liked.  A couple stood out more than others as they seemed to hit the target on the first go around based on our brief and sample sites submitted.

There are several designers we would like to work with in the future as well as we have about 40 domains we will be developing.

Thank you.

Target Market(s)

Target Market: Female, typically 25-40 yrs old, probably married, probably career minded OR middle to upper middle income (some of our strollers are $500-$1,200), expecting mom or mom, some might have two stroller aged (double strollers). Some of our products are QUALITY (ZEK for jogging or running) or QUALITY with STYLE (Quillaro), but the truth is that this is a WANT not a need. Sure people need A stroller but not a $900 Tessel Stroller. So they have a combination of want and need coupled with ability to pay.

Brand Personality:
Definitely clean, crisp and modern. We want it to “POP” but in color and style. But I guess more directly is we want to be seen as THE or ONE of THE authorities on upper end strollers. Where you can get individual assistance, stroller consultations (yes people call in with their needs and ask advice) and personalized service as opposed to a “big box” type place that tries to be everything to everyone and when you call them you get some guy in a cubicle answering the phone that held his baby niece once. So when someone hits our site or walks into our showroom, they need to know they are in the right place.

Industry/Entity Type

Baby

Requirements
Must have
• Must a clean crisp color scheme, easy to ready, focused on products. Must instill authority, credibility, usability and be simple and uncluttered. Fonts and colors must complement each other to achieve the above.

We need three main images as well for the home page as they will be sliding/rotating images.

Backend is built in Magento so design must conform to that platform.

We retain exlusive rights to the design and all files
Nice to have
• Please see attached word file for more info.

Here are some sites we like:

www.tinyharbor.com
http://www.cubnook.com/
http://www.dapwick.com/
http://www.vemakids.com/index.php
http://www.fernwax.com/
http://www.tana-lume.com/
http://www.grelby.com/
http://www.cardsmithpartners.com/

Keep in mind that I may just like only something about the above sites and not everything. It may be color, it may be layout , font color, use of text on home page, but something about them stands out.

Here are a few like companies:

www.pramvault.com
www.buggynest.com
www.tiddlytopkids.com
www.kplums.com
www.wrenandtilly.com
www.doravimo.com
Should not have
• old dated styles, nothing "frilly"

```html
<!DOCTYPE html>
<html lang="en">
<head>
<meta charset="utf-8">
<title>Happy Wheel Walks – Home</title>
<link href="https://fonts.googleapis.com/css2?family=Open+Sans:wght@400;600;700&display=swap" rel="stylesheet">
<style>
:root{
  --pink:#e4356a;
  --teal:#2fb1bf;
  --text:#444;
  --muted:#777;
  --line:#d9d9d9;
  --page-bg:#f2f2f2;
  --white:#fff;
  --tab-top:#e9e9e9;
  --tab-bottom:#cfcfcf;
  --footer-bg:#e3e1e1;
  --footer-bar:#cbc9c9;
  --star:#c8323c;
  --price:#d7262f;
}
*{box-sizing:border-box;margin:0;padding:0}
html,body{width:1200px;height:900px;overflow:hidden}
body{background:var(--page-bg);font-family:"Open Sans",Arial,sans-serif;color:var(--text);position:relative}
.page{position:absolute;left:104px;top:0;width:1004px;height:900px;background:var(--white)}
.abs{position:absolute}

/* sidebar */
.sidebar-top{left:116px;top:0;width:218px;height:28px;border:1px solid var(--line);border-top:none;background:var(--white)}
.refine{left:116px;top:40px;width:218px;height:418px;border:1px solid var(--line);background:var(--white)}
.refine h2{position:absolute;left:14px;top:12px;font-size:22px;font-weight:400;color:var(--pink)}
.refine .rule{position:absolute;left:0;right:0;top:52px;border-top:1px solid var(--line)}
.refine h3{position:absolute;left:14px;font-size:13px;font-weight:700;color:#333}
.refine ul{position:absolute;left:14px;list-style:none}
.refine li{font-size:11.5px;height:28px;line-height:28px;color:var(--muted)}
.refine li::before{content:"›";color:#aaa;margin-right:8px;font-size:13px}
.refine li.active{color:var(--pink)}
.refine .see-all{position:absolute;left:26px;top:207px;font-size:11px;color:var(--teal);text-decoration:underline}

/* top strip */
.hero-strip{top:0;height:24px}
.news{left:356px;top:30px;width:420px;height:76px;border:1px solid var(--line);background:#f7f7f7;overflow:hidden}
.news-tag{position:absolute;left:0;top:0}
.news p{position:absolute;left:96px;top:16px;width:200px;font-size:11px;line-height:18px;color:#444}
.news .blog{position:absolute;left:358px;top:18px;font-size:27px;font-weight:600;color:var(--pink)}
.news svg.arrow{position:absolute;left:314px;top:20px}
.newsletter{left:790px;top:30px;width:306px;height:76px;border:1px solid var(--line);background:#f7f7f7}
.newsletter h2{position:absolute;left:20px;top:8px;font-size:20px;font-weight:400;color:var(--pink)}
.newsletter .field{position:absolute;left:24px;top:42px;width:206px;height:22px;background:var(--white);border:1px solid #ccc}
.newsletter .go{position:absolute;left:244px;top:36px;width:34px;height:34px;border-radius:50%;background:var(--pink);color:var(--white);font-size:14px;font-weight:600;text-align:center;line-height:34px}

/* section headers */
.section-head{left:356px;width:740px;height:50px;border-bottom:1px solid var(--line)}
.section-head .tab{position:absolute;left:0;top:0;width:226px;height:50px;background:linear-gradient(var(--tab-top),var(--tab-bottom))}
.section-head .tab svg{position:absolute;left:8px;top:12px}
.section-head h2{position:absolute;left:44px;top:11px;font-size:20px;font-weight:400;color:#333}

/* product row */
.circle-arrow{width:26px;height:26px;border-radius:50%;background:#ddd;color:var(--white);font-size:18px;text-align:center;line-height:24px;font-weight:700}
.card{top:184px;width:156px;height:214px;border:1px solid var(--line);background:var(--white)}
.card .photo{position:absolute;left:24px;top:12px;width:108px;height:128px;border-radius:6px}
.card .name{position:absolute;left:28px;top:150px;font-size:13px;color:#333}
.card .stars{position:absolute;left:28px;top:168px;font-size:15px;color:var(--star);letter-spacing:1px}
.card .reviews{position:absolute;left:28px;top:190px;font-size:12px;color:#333}
.price{left:446px;top:270px;width:66px;height:66px;border-radius:50%;background:var(--price);border:2px dashed rgba(255,255,255,.7);color:var(--white);font-size:14px;text-align:center;line-height:62px;z-index:2}

/* brands */
.brand{top:514px;width:110px;text-align:center;font-size:17px;font-weight:700;color:#222;white-space:nowrap}
.chev{top:520px;font-size:36px;color:#ccc;line-height:20px}
.brand-rule{left:356px;top:590px;width:740px;border-top:1px solid var(--line)}

/* footer */
.footer{left:116px;top:632px;width:980px;height:268px;background:var(--footer-bg)}
.footer-col{top:646px}
.footer-col h3{font-size:14.5px;font-weight:700;color:var(--pink);margin-bottom:6px}
.footer-col h3.alt{color:var(--teal);margin-top:10px}
.footer-col a{display:block;font-size:11.5px;line-height:18px;color:#444;text-decoration:none}
.footer-bar{left:116px;top:852px;width:980px;height:48px;background:linear-gradient(var(--footer-bar),#bdbbbb)}
.footer-bar .copy{position:absolute;left:40px;top:16px;font-size:11.5px;font-weight:600;color:#333;white-space:nowrap}
.footer-bar .follow{position:absolute;left:408px;top:15px;font-size:12.5px;color:#333;white-space:nowrap}
.social{position:absolute;top:12px;width:24px;height:24px;border-radius:3px}
</style>
</head>
<body>
<div class="page"></div>

<!-- sidebar -->
<div class="abs sidebar-top"></div>
<aside class="abs refine">
  <h2>Refine Results</h2>
  <div class="rule"></div>
  <h3 style="top:64px">Brand</h3>
  <ul style="top:86px">
    <li class="active">Tot Trekker (6)</li>
    <li>ZEK (45)</li>
    <li>Meadow Carriers (11)</li>
    <li>Pedalo Kids (2)</li>
  </ul>
  <span class="see-all">See All Brands</span>
  <h3 style="top:254px">Best Use</h3>
  <ul style="top:280px">
    <li>Casual (8)</li>
    <li>Cross-training (2)</li>
    <li>Cycling (47)</li>
    <li>Running (5)</li>
  </ul>
</aside>

<!-- top strip -->
<div class="abs hero-strip" style="left:356px;width:340px;background:linear-gradient(90deg,#ead7cf,#f3e6df)" role="img" aria-label="Lifestyle photo of a family with a stroller"></div>
<div class="abs hero-strip" style="left:706px;width:390px;background:linear-gradient(90deg,#f1e2de,#e6d2cc)" role="img" aria-label="Lifestyle photo of a mother with her baby"></div>

<section class="abs news">
  <svg class="news-tag" width="94" height="76" viewBox="0 0 94 76">
    <polygon points="0,38 68,0 94,0 94,7.5 0,60" fill="var(--teal)"/>
    <text transform="translate(12,47) rotate(-29.2)" font-family="Open Sans,Arial,sans-serif" font-size="15" font-weight="600" fill="#fff">News</text>
  </svg>
  <p>Lorem Ipsum is simply dummy text of the printing and typesetting industry. Lorem Ipsum has been …</p>
  <svg class="arrow" width="34" height="36" viewBox="0 0 34 36"><polygon points="0,0 14,0 34,18 14,36 0,36 20,18" fill="#555"/></svg>
  <span class="blog">Blog</span>
</section>
<section class="abs newsletter">
  <h2>Sign Up for Our Newsletter</h2>
  <div class="field"></div>
  <div class="go">Go</div>
</section>

<!-- featured products -->
<div class="abs section-head" style="top:118px">
  <div class="tab"><svg width="26" height="26" viewBox="0 0 24 24"><polygon points="12,2 15,9 22,9.5 16.5,14 18.5,21 12,17 5.5,21 7.5,14 2,9.5 9,9" fill="#bbb"/></svg></div>
  <h2>Featured Products</h2>
</div>
<div class="abs circle-arrow" style="left:354px;top:278px">‹</div>
<div class="abs circle-arrow" style="left:1068px;top:278px">›</div>

<div class="abs card" style="left:394px">
  <div class="photo" role="img" aria-label="Teal and brown quilted diaper bag" style="background:linear-gradient(#3fa7a4,#5b3b2c)"></div>
  <div class="name">Name Lorem Ipsum</div><div class="stars">★★★★☆</div><div class="reviews">(1 Review)</div>
</div>
<div class="abs price">$50.00</div>
<div class="abs card" style="left:562px">
  <div class="photo" role="img" aria-label="Pink messenger diaper bag" style="background:linear-gradient(#f4a3c8,#e27aab)"></div>
  <div class="name">Name Lorem Ipsum</div><div class="stars">★★★★☆</div><div class="reviews">(1 Review)</div>
</div>
<div class="abs card" style="left:730px">
  <div class="photo" role="img" aria-label="Multicolour striped tote bag" style="background:linear-gradient(90deg,#3a6e3a,#d9a030,#3a78b0,#c04a3a)"></div>
  <div class="name">Name Lorem Ipsum</div><div class="stars">★★★★☆</div><div class="reviews">(1 Review)</div>
</div>
<div class="abs card" style="left:898px">
  <div class="photo" role="img" aria-label="Red and black modern stroller" style="background:linear-gradient(#d8333a,#333)"></div>
  <div class="name">Name Lorem Ipsum</div><div class="stars">★★★★☆</div><div class="reviews">(1 Review)</div>
</div>

<!-- featured brands -->
<div class="abs section-head" style="top:426px">
  <div class="tab"><svg width="26" height="26" viewBox="0 0 24 24"><polygon points="12,2 15,9 22,9.5 16.5,14 18.5,21 12,17 5.5,21 7.5,14 2,9.5 9,9" fill="#bbb"/></svg></div>
  <h2>Featured Brands</h2>
</div>
<div class="abs chev" style="left:358px">‹</div>
<div class="abs chev" style="left:1074px">›</div>
<span class="abs brand" style="left:378px">Tot Trekker</span>
<span class="abs brand" style="left:490px">ZEK</span>
<span class="abs brand" style="left:622px">Quillaro</span>
<span class="abs brand" style="left:734px">Sugarpod</span>
<span class="abs brand" style="left:846px">Lumo</span>
<span class="abs brand" style="left:958px">Vantor</span>
<div class="abs brand-rule"></div>

<!-- footer -->
<footer class="abs footer"></footer>
<div class="abs footer-col" style="left:176px">
  <h3>Happy Wheel Walks</h3>
  <a>About Trailhaus</a><a>Jobs at Trailhaus</a><a>100% Satisfaction</a><a>Guarantee</a><a>Corporate &amp; Group Sales</a><a>Privacy Policy</a><a>Terms of Use</a><a>Site Rules</a>
</div>
<div class="abs footer-col" style="left:400px">
  <h3>Become a Seller</h3>
  <a>Become a Trailhaus Member</a><a>Member Help</a><a>Find Membership Number</a>
  <h3 class="alt">More Useful Links</h3>
  <a>Lorem Ipsum</a><a>Dolor Sit Amet</a><a>Tandem Donec</a>
</div>
<div class="abs footer-col" style="left:692px">
  <h3>Stroller Expert</h3>
  <a>Stroller Expert Articles</a><a>Lorem Ipsum Sit</a><a>Donec Tandem Quosque</a>
  <h3 class="alt">More Useful Links</h3>
  <a>Lorem Ipsum</a><a>Dolor Sit Amet</a><a>Tandem Donec</a>
</div>
<div class="abs footer-col" style="left:894px">
  <h3>Help</h3>
  <a>Help Section</a><a>Contact Us</a><a>Live Help</a><a>Order Status</a><a>Returns &amp; Exchanges</a><a>Product Safety</a><a>Shipping Info</a><a>Another link</a>
</div>
<div class="abs footer-bar">
  <span class="copy">© 2011 Happy Wheel Walks. All Rights Reserved.</span>
  <span class="follow">For The Latest News and Special Offers, Follow Us:</span>
  <span class="social" style="left:764px;background:#4ab3e0"></span>
  <span class="social" style="left:792px;background:#3b5a9a"></span>
  <span class="social" style="left:820px;background:#c4302b"></span>
  <span class="social" style="left:848px;background:#2a7bb6"></span>
  <span class="social" style="left:876px;background:#3f8f3a"></span>
</div>
</body>
</html>
```